Roofing & Siding door hanger flyer

-Looking to make door hanger flyer for Pellmont Roofing & Siding
-4.5" wide x 11" tall
-2 sided full colour
-We have started a new website (the content is changing) I have attached photos.
-About us:
-25 year labour warranty's available
-32 years in Calgary
-QCR A+ Member
-NWTG (Prairie Joint Shingle Guild) (logo attached)
-KOV Summit Select (logo attached)
-Owen Brisket (logo attached)
-Slogan "Raised On Care, Proven Through Seasons" 32 years in Calgary
-Sale
-Page 1 & 2 design ideas
We are in your area, contact us today for your Exclusive limited time offer! *discounts apply exclusively to new agreements only
Updates
-Please keep simple, clean & bright
-I really like the bright blue from our new logo (new logo uploaded)
-We specialize in Roofing -Siding-Gutters & full Exterior Renos (like the competitor example uploaded)
-This is the NEW website we are currently working on (not finished) https://mockview.example-draftpad.net/view/1a2b3c4d-5e6f-4a7b-8c9d-0e1f2a3b4c5d-7k2m/?fullscreen
-This is our OLD website https://pellmontshingleworks.com
-For the sale "We are in your area, contact us today for your Exclusive limited time offer" *discounts apply exclusively to new agreements only
-Free Estimates
-our phone# is 403-555-0148
-our website is pellmontshingleworks.com
-keep simple, clean, bright use the "new logo" uploaded. Check out the competitor example uploaded file
-We are in your area, Contact us today for your Exclusive limited time offer! *discounts apply to new agreements only
-FREE ESTIMATES
-Specialized in Roofing /Siding /Gutters Full Exterior Reno's
-We are currently working on a NEW website https://mockview.example-draftpad.net/view/1a2b3c4d-5e6f-4a7b-8c9d-0e1f2a3b4c5d-7k2m/?fullscreen
-Our OLD website https://pellmontshingleworks.com/
-Post old site address on flyer pellmontshingleworks.com
-Phone # 403-555-0148
Target Market(s)
40-55
Industry/Entity Type
Roofing Siding & full Exterior Reno's
Look and feel

```html
<!DOCTYPE html>
<html lang="en">
<head>
<meta charset="utf-8">
<title>Pellmont Roofing &amp; Siding – Door Hanger</title>
<link href="https://fonts.googleapis.com/css2?family=Poppins:wght@500;600;700;800&family=Montserrat:wght@500;600&display=swap" rel="stylesheet">
<style>
  :root{
    --stage:#808183;
    --blue:#1367b8;
    --red:#d3222a;
    --ink:#1d1d1f;
    --charcoal:#333335;
    --white:#ffffff;
    --gold:#c99a2e;
    --navy:#1f3a7a;
    --green:#2c9a48;
  }
  *{box-sizing:border-box;margin:0;padding:0}
  html,body{width:1200px;height:848px;overflow:hidden}
  body{background:var(--stage);position:relative;font-family:"Poppins",sans-serif}

  .hanger{
    position:absolute;top:81px;width:280px;height:686px;background:var(--white);overflow:hidden;
    clip-path:path('M14,0 H266 A14,14 0 0 1 280,14 V672 A14,14 0 0 1 266,686 H14 A14,14 0 0 1 0,672 V126 Q0,91 36,91 H129 A42,42 0 1 0 129,76 H22 Q0,76 0,54 V14 A14,14 0 0 1 14,0 Z');
  }
  .hanger--front{left:275px}
  .hanger--back{left:644px}
  .abs{position:absolute}

  /* front */
  .hero-fade{left:0;top:0;width:280px;height:227px;background:linear-gradient(180deg,#e4edf6 0%,#eef1f4 55%,#e5ebe0 100%)}
  .kicker{left:0;width:280px;top:10px;text-align:center;font:600 11px/1 "Montserrat",sans-serif;color:var(--ink);letter-spacing:.3px}
  .headline{left:0;width:280px;top:22px;text-align:center;font:800 23.5px/1 "Poppins",sans-serif;color:var(--blue);letter-spacing:-.3px}
  .brand{left:0;width:280px;text-align:center;font:700 31px/1 "Poppins",sans-serif;color:var(--ink);letter-spacing:1px}
  .brand-sub{display:block;font-size:11.5px;letter-spacing:3px;margin-top:5px}
  .hanger--front .brand{top:160px}

  .band{left:0;width:280px;height:10px;background:var(--blue);z-index:2}
  .tab{height:24px;background:var(--blue);color:var(--white);font:700 14.5px/24px "Poppins",sans-serif;text-align:center;border-radius:0 0 12px 12px;letter-spacing:.4px;z-index:3}
  .photo-roof{left:150px;top:237px;width:130px;height:99px;z-index:1;background:linear-gradient(135deg,#e6ecf2 0%,#4a4f57 45%,#b86a3e 100%)}
  .photo-siding{left:168px;top:347px;width:112px;height:100px;z-index:1;background:linear-gradient(135deg,#eef1f5 0%,#5a6170 55%,#2f3440 100%)}

  .checks{list-style:none;color:var(--blue);font:700 10.3px/1 "Poppins",sans-serif;z-index:2}
  .checks li{position:absolute;left:0;white-space:nowrap;display:flex;align-items:flex-start;gap:2px}
  .checks li svg{width:9px;height:9px;flex:none;margin-top:1px}
  .checks--roofing{left:19px;top:272px}
  .checks--siding{left:19px;top:370px}
  .checks--ext{left:19px;top:484px}
  .checks--ext2{left:146px;top:482px}

  .phone{left:0;width:280px;text-align:center;color:var(--red);font:700 33px/1 "Poppins",sans-serif;letter-spacing:-.3px}
  .hanger--front .phone{top:584px}
  .web{left:0;width:280px;text-align:center;font:500 11.4px/1 "Montserrat",sans-serif;color:var(--ink)}
  .hanger--front .web{top:656px}
  .foot{left:0;top:674px;width:280px;height:12px;background:var(--blue)}

  /* back */
  .photo-home{left:0;top:0;width:281px;height:227px;background:linear-gradient(180deg,#4f86c6 0%,#b7bfc7 40%,#8c8f8f 62%,#5f8f3a 85%,#4f7d2e 100%)}
  .seal{left:190px;top:196px;width:52px;height:52px;border-radius:50%;background:var(--gold);z-index:2}
  .offer{left:0;top:227px;width:281px;height:109px;background:var(--blue);color:var(--white);text-align:center}
  .offer-lead{position:absolute;left:0;width:100%;top:9px;font:600 8.8px/1 "Poppins",sans-serif;letter-spacing:.3px}
  .offer-title{position:absolute;left:0;width:100%;top:26px;font:700 16.3px/19.5px "Poppins",sans-serif;letter-spacing:.4px}
  .offer-note{position:absolute;left:0;width:100%;top:90px;font:500 8px/1 "Poppins",sans-serif;letter-spacing:.2px}
  .special{left:0;top:336px;width:281px;height:35px;background:var(--charcoal);color:var(--white);text-align:center;font:700 24px/35px "Poppins",sans-serif;letter-spacing:.8px}
  .checks--services{left:19px;top:393px;color:var(--ink);font-size:11.6px}
  .checks--services li svg{width:10px;height:10px}
  .cert{left:205px;top:397px;width:48px;height:48px}
  .partner-dot{left:220px;top:460px;width:18px;height:18px;border-radius:50%;background:var(--green)}
  .partner{left:180px;width:100px;top:482px;text-align:center;font:700 10px/1 "Poppins",sans-serif;color:var(--ink)}
  .rule{left:20px;top:514px;width:240px;height:1px;background:var(--ink)}
  .hanger--back .brand{top:538px;font-size:24px}
  .hanger--back .brand-sub{font-size:9px;letter-spacing:2.5px;margin-top:3px}
  .free{left:0;width:281px;top:599px;text-align:center;font:700 11.8px/1 "Poppins",sans-serif;color:var(--ink)}
  .hanger--back .phone{top:617px;font-size:29px;width:281px}
  .hanger--back .web{top:653px;width:281px;font:700 11px/1 "Poppins",sans-serif}
  .hanger--back .foot{width:281px}
</style>
</head>
<body>
<svg width="0" height="0" style="position:absolute" aria-hidden="true">
  <defs>
    <symbol id="tick" viewBox="0 0 10 10">
      <rect x="0.7" y="1.2" width="7.6" height="7.6" fill="none" stroke="currentColor" stroke-width="1.3"/>
      <path d="M2.3 4.8 L4.2 6.8 L9.4 0.8" fill="none" stroke="currentColor" stroke-width="1.5"/>
    </symbol>
  </defs>
</svg>

<section class="hanger hanger--front">
  <div class="abs hero-fade" role="img" aria-label="Faded photo of a white two-storey house with porch and lawn"></div>
  <p class="abs kicker">WE’RE IN YOUR</p>
  <h1 class="abs headline">NEIGHBOURHOOD!</h1>
  <p class="abs brand">PELLMONT<span class="brand-sub">ROOFING &amp; SIDING</span></p>

  <div class="abs photo-roof" role="img" aria-label="Photo of a dark metal roof over a red brick gable"></div>
  <div class="abs band" style="top:227px"></div>
  <div class="abs tab" style="left:88px;top:231px;width:105px">ROOFING</div>
  <ul class="abs checks checks--roofing">
    <li style="top:0"><svg><use href="#tick"/></svg>Asphalt</li>
    <li style="top:20px"><svg><use href="#tick"/></svg>Rubber</li>
    <li style="top:40px"><svg><use href="#tick"/></svg>Metal</li>
  </ul>

  <div class="abs photo-siding" role="img" aria-label="Photo of a modern house with white board and dark siding"></div>
  <div class="abs band" style="top:336px;height:11px"></div>
  <div class="abs tab" style="left:94px;top:339px;width:91px">SIDING</div>
  <ul class="abs checks checks--siding">
    <li style="top:0"><svg><use href="#tick"/></svg>Brisket fibre cement</li>
    <li style="top:20px"><svg><use href="#tick"/></svg>Vinyl</li>
    <li style="top:40px"><svg><use href="#tick"/></svg>Metal (Steel, Aluminum)</li>
    <li style="top:60px"><svg><use href="#tick"/></svg>Longboard</li>
  </ul>

  <div class="abs band" style="top:447px;height:11px"></div>
  <div class="abs tab" style="left:63px;top:449px;width:153px">FULL EXTERIORS</div>
  <ul class="abs checks checks--ext">
    <li style="top:0"><svg><use href="#tick"/></svg><span>Eaves trough |<br>Soffir | Fascia</span></li>
    <li style="top:32px"><svg><use href="#tick"/></svg>Stone</li>
    <li style="top:53px"><svg><use href="#tick"/></svg>Skylights</li>
    <li style="top:73px"><svg><use href="#tick"/></svg>Windows &amp; Doors</li>
  </ul>
  <ul class="abs checks checks--ext2">
    <li style="top:0"><svg><use href="#tick"/></svg>Stucco</li>
    <li style="top:21px"><svg><use href="#tick"/></svg>Insulation</li>
    <li style="top:41px"><svg><use href="#tick"/></svg>Painting</li>
    <li style="top:61px"><svg><use href="#tick"/></svg>Shake Prepairs</li>
  </ul>

  <p class="abs phone">(403) 555-0148</p>
  <p class="abs web">www.pellmontshingleworks.com</p>
  <div class="abs foot"></div>
</section>

<section class="hanger hanger--back">
  <div class="abs photo-home" role="img" aria-label="Photo of a family sitting on the lawn in front of their house"></div>
  <div class="abs offer">
    <p class="offer-lead">We are in your area</p>
    <h2 class="offer-title">CONTACT US TODAY FOR<br>YOUR EXCLUSIVE LIMITED<br>TIME OFFER!</h2>
    <p class="offer-note">*discounts apply to new agreements only</p>
  </div>
  <div class="abs seal" role="img" aria-label="Anniversary seal"></div>
  <h2 class="abs special">SPECIALIZED IN</h2>
  <ul class="abs checks checks--services">
    <li style="top:0"><svg><use href="#tick"/></svg>ROOFING</li>
    <li style="top:30px"><svg><use href="#tick"/></svg>SIDING</li>
    <li style="top:59px"><svg><use href="#tick"/></svg>GUTTERS</li>
    <li style="top:89px"><svg><use href="#tick"/></svg>FULL EXTERIOR RENO’S</li>
  </ul>
  <svg class="abs cert" viewBox="0 0 48 48" role="img" aria-label="KOV Summit Select certification badge">
    <path d="M24 1 L47 24 L24 47 L1 24 Z" fill="var(--navy)"/>
  </svg>
  <div class="abs partner-dot"></div>
  <p class="abs partner">Owen Brisket</p>
  <div class="abs rule"></div>
  <p class="abs brand">PELLMONT<span class="brand-sub">ROOFING &amp; SIDING</span></p>
  <p class="abs free">FREE ESTIMATES</p>
  <p class="abs phone">(403) 555–0148</p>
  <p class="abs web">www.pellmontshingleworks.com</p>
  <div class="abs foot"></div>
</section>
</body>
</html>
```